Business Card Design Project

Need a business card with logo that is attached.
Company name: Tolmen Brisk Solutions, LLC
My name: Lorna Tolmen
Title: President
Phone number: 703-555-0148
Email: ltolmen@tolmenbrisksolutions.example
web site: www.tolmenbrisksolutions.example

Industry/Entity Type

Business

```html
<!DOCTYPE html>
<html lang="en">
<head>
<meta charset="utf-8">
<title>Tolmen Brisk Solutions, LLC — Business Card</title>
<link rel="stylesheet" href="https://fonts.googleapis.com/css2?family=Tinos:wght@400;700&display=swap">
<style>
  :root {
    --bg-top: #ff8985;
    --bg-blush: #fbd6d2;
    --bg-cream: #f9f1d6;
    --bg-mint: #e4f8c9;
    --bg-green: #b8f1c2;
    --bg-bottom: #4de0da;
    --ink: #0b0b0b;
    --shadow: rgba(0, 0, 0, 0.45);
    --ornament-tone: rgba(11, 11, 11, 0.16);
  }

  html, body {
    margin: 0;
    padding: 0;
    width: 1200px;
    height: 720px;
    overflow: hidden;
  }

  .card {
    position: relative;
    width: 1200px;
    height: 720px;
    overflow: hidden;
    font-family: "Tinos", "Times New Roman", serif;
    color: var(--ink);
    background: linear-gradient(
      to bottom,
      var(--bg-top) 0%,
      var(--bg-blush) 30%,
      var(--bg-cream) 45%,
      var(--bg-mint) 62%,
      var(--bg-green) 80%,
      var(--bg-bottom) 100%
    );
  }

  .holder {
    position: absolute;
    left: 56px;
    top: 50px;
    width: 250px;
    margin: 0;
    text-align: center;
    font-weight: 700;
    text-transform: uppercase;
    line-height: 1.3;
    text-shadow: 2px 2px 3px var(--shadow);
  }

  .holder-title {
    display: block;
    font-size: 26px;
    letter-spacing: 0.5px;
  }

  .holder-name {
    display: block;
    font-size: 24px;
  }

  .brand {
    position: absolute;
    left: 0;
    right: 0;
    top: 222px;
    margin: 0;
  }

  .company-name {
    margin: 0;
    text-align: center;
    font-size: 56px;
    font-weight: 700;
    line-height: 1;
    color: var(--ink);
  }

  .brand-ornament {
    position: absolute;
    left: 318px;
    top: 114px;
    width: 564px;
    height: 107px;
    border-radius: 54px;
    background: radial-gradient(ellipse at center, rgba(11, 11, 11, 0.24) 0%, var(--ornament-tone) 55%, rgba(11, 11, 11, 0.04) 100%);
  }

  .contact-line {
    position: absolute;
    left: 0;
    right: 0;
    top: 658px;
    margin: 0;
    text-align: center;
    white-space: nowrap;
    font-size: 20px;
    font-weight: 700;
  }
</style>
</head>
<body>
  <main class="card">
    <p class="holder">
      <span class="holder-title">President</span>
      <span class="holder-name">Lorna Tolmen</span>
    </p>

    <div class="brand">
      <h1 class="company-name">Tolmen Brisk Solutions, LLC</h1>
      <div class="brand-ornament" role="img" aria-label="Symmetrical black scrollwork flourish beneath the company name"></div>
    </div>

    <p class="contact-line">703-555-0148, E-mail: ltolmen@tolmenbrisksolutions.example, Website: http://tolmenbrisksolutions.example</p>
  </main>
</body>
</html>
```